Harbor Circuits LLC is a Minneapolis / St Paul and surrounding communities computer repair and service company. It serves residential and small businesses. We work primarily with virus removal, data recovery, system baselines, networking, and new system installation. The site should look clean, professional, and easy to navigate.

This wordpress project must be coded and integrated into a wordpress theme for easy upload and maintenance.
Updates

Designers - Please make sure your design is in a wordpress theme so that It can be uploaded.  

Thank you,

Brent 

Target Market(s)

Residential and Small Business

Industry/Entity Type

Residential

Requirements
Must have
• Site Content
1. Main Page should have photos that scroll across, Business Description, Space to run
“Specials” Ads
a. Intuitive Navigation
2. Additional Pages
a. Blog for Computer Repair Articles
b. Testimonials Page
c. Contact Pages
d. Services Page with the ability to put in pricing
3. The site must be clean and professional.
4. Wordpress Theme

```html
<!DOCTYPE html>
<html lang="en">
<head>
<meta charset="utf-8">
<title>Harbor Circuits LLC — PC Repair & Support</title>
<link href="https://fonts.googleapis.com/css2?family=Roboto+Condensed:wght@300;400;700&family=Josefin+Sans:wght@400&family=Open+Sans:wght@400;700&family=Arimo:wght@400;700&display=swap" rel="stylesheet">
<style>
:root{
  --black:#050505;
  --header-top:#f4f4f4;
  --header-bottom:#d9d9d9;
  --nav:#2a2a2a;
  --nav-text:#8a8a8a;
  --green:#5aa12a;
  --green-light:#80c356;
  --green-dark:#3f8a1c;
  --panel:#ececec;
  --ink:#333;
  --grey-text:#4a4a4a;
  --footer:#333;
  --footer-link:#9fc6c9;
  --orange:#e8531d;
}
*{box-sizing:border-box;margin:0;padding:0}
html,body{width:1150px;height:1200px;overflow:hidden}
body{position:relative;background:#fff;font-family:"Arimo",Arial,sans-serif;color:var(--ink)}
.abs{position:absolute}
.topbar{left:0;top:0;width:1150px;height:18px;background:var(--black)}
.masthead{left:0;top:18px;width:1150px;height:93px;background:linear-gradient(var(--header-top),var(--header-bottom))}
.brand{left:168px;top:24px;display:flex;align-items:center;gap:12px}
.brand-mark{width:76px;height:76px;border-radius:50%;border:4px solid var(--green)}
.brand-name{font-family:"Roboto Condensed",sans-serif;font-weight:700;font-size:34px;color:#4a4a4a;white-space:nowrap}
.callout-photo{left:698px;top:22px;width:64px;height:86px;background:linear-gradient(#5b5b5b,#1d1d1d);border-radius:4px}
.callout{left:774px;top:30px;width:214px;height:71px;background:#fff;padding:5px 5px;white-space:nowrap;overflow:hidden}
.callout h3{font-family:"Roboto Condensed",sans-serif;font-weight:700;font-size:18px;color:var(--green);line-height:21px}
.callout p{font-family:"Open Sans",sans-serif;font-size:11.5px;line-height:15px;color:#222}
.callout strong{font-family:"Open Sans",sans-serif;font-weight:700;font-size:14px;line-height:20px;display:block;margin-top:4px;color:#111}
.nav{left:0;top:111px;width:1150px;height:38px;background:repeating-linear-gradient(135deg,#2e2e2e 0 2px,#222 2px 4px)}
.nav ul{position:absolute;left:164px;top:0;display:flex;list-style:none;height:38px}
.nav li{font-family:"Open Sans",sans-serif;font-weight:700;font-size:12.5px;color:var(--nav-text);padding:0 18px;line-height:38px;border-right:1px solid #444;white-space:nowrap}
.nav li.active{background:var(--green);color:#fff;padding:0 27px}
.nav li:last-child{border-right:0}
.page{left:153px;top:149px;width:842px;height:874px;background:#fff;box-shadow:0 0 4px rgba(0,0,0,.25)}
.hero{left:159px;top:155px;width:827px;height:272px;background:var(--panel)}
.hero h1{position:absolute;left:14px;top:20px;font-family:"Josefin Sans",sans-serif;font-weight:400;font-size:44px;color:#2d2d2d;letter-spacing:-1px;white-space:nowrap}
.hero h2{position:absolute;left:15px;top:66px;font-family:"Roboto Condensed",sans-serif;font-weight:400;font-size:24px;color:var(--green);white-space:nowrap}
.hero ul{position:absolute;left:32px;top:101px;list-style:disc;font-size:12.5px;color:var(--grey-text);line-height:22px;white-space:nowrap}
.hero .more{position:absolute;left:16px;top:206px;font-family:"Roboto Condensed",sans-serif;font-size:17px;color:#444;white-space:nowrap}
.hero .more b{color:var(--green);font-size:24px;font-weight:700}
.hero .pkg{position:absolute;left:226px;top:193px;transform:rotate(-20deg);font-family:"Roboto Condensed",sans-serif;color:var(--orange);font-size:26px;font-weight:700}
.hero .starts{position:absolute;left:234px;top:228px;transform:rotate(-20deg);font-family:"Roboto Condensed",sans-serif;font-size:13px;color:#333}
.hero .price{position:absolute;left:347px;top:183px;font-family:"Roboto Condensed",sans-serif;font-size:64px;color:var(--green);font-weight:400}
.hero .price span{font-size:34px;color:#555;vertical-align:4px;margin-right:2px}
.hero .arrow{position:absolute;left:334px;top:164px}
.hero-art{left:477px;top:40px;width:340px;height:200px;background:radial-gradient(ellipse at 60% 70%,#7b8a99 0,#c9c9c9 55%,var(--panel) 75%)}
.tab{height:41px;background:linear-gradient(#606060,#474747);border:1px solid #3a3a3a;text-align:center;font-family:"Roboto Condensed",sans-serif;font-weight:300;font-size:25px;color:#fff;line-height:40px;white-space:nowrap}
.tab::after{content:"";position:absolute;left:118px;bottom:-9px;border-left:12px solid transparent;border-top:9px solid #474747}
.tab-services{left:164px;top:435px;width:259px}
.tab-welcome{left:469px;top:435px;width:517px}
.tab-welcome::after{left:210px}
.services-box{left:165px;top:494px;width:256px;height:500px;background:var(--panel);border:1px solid #d4d4d4}
.services-box ul{list-style:none;margin:6px 5px 0}
.services-box li{font-size:11.5px;color:#333;border-bottom:1px dashed #a0a0a0;height:29px;line-height:30px;padding-left:20px;position:relative;white-space:nowrap}
.services-box li::before{content:"›";position:absolute;left:6px;top:-1px;font-weight:700}
.testimonial{left:175px;top:743px;width:233px;height:234px;background:linear-gradient(var(--green),var(--green-light));border:1px solid var(--green-dark);color:#fff;padding:12px 13px}
.testimonial h3{font-family:"Roboto Condensed",sans-serif;font-weight:300;font-size:25px}
.testimonial .who{display:flex;gap:8px;margin:6px 0 4px 2px;font-size:9.5px;line-height:14px;color:#111}
.testimonial .avatar{width:40px;height:40px;background:linear-gradient(#8b6f5e,#3e3530)}
.testimonial .quote{font-size:9.5px;line-height:15px}
.testimonial .read{display:block;margin-top:17px;font-size:10px;font-weight:700}
.welcome{left:468px;top:493px;width:510px;font-size:9.5px;line-height:15px;color:#333}
.welcome p{margin-bottom:4px}
.rule{left:459px;top:705px;width:527px;height:1px;background:#999}
.fixed h2{position:absolute;left:467px;top:722px;font-family:"Roboto Condensed",sans-serif;font-size:20px;font-weight:400;color:#444;white-space:nowrap}
.fixed p{position:absolute;left:469px;top:755px;width:265px;font-size:9.5px;line-height:15px;color:#333}
.btn{left:469px;width:248px;height:33px;background:linear-gradient(var(--green-light),var(--green));border:1px solid var(--green-dark);border-radius:2px;font-family:"Roboto Condensed",sans-serif;font-weight:300;font-size:19px;color:#fff;text-align:center;line-height:32px}
.ad{left:766px;top:719px;width:206px;height:205px;background:linear-gradient(#1f3a55,#3a2a4c 60%,#0c0c0c)}
.footer{left:0;top:1023px;width:1150px;height:177px;background:var(--footer);color:#fff}
.footer h3{position:absolute;font-family:"Roboto Condensed",sans-serif;font-weight:300;font-size:20px}
.blog{left:164px;width:254px;top:41px}
.blog a{display:block;font-size:9.5px;font-weight:700;color:var(--footer-link);line-height:15px;padding:4px 2px 8px;border-bottom:1px solid #888;margin-bottom:4px}
.vsep{top:7px;width:1px;height:145px;background:#222}
.news{left:451px;top:40px;width:255px}
.news h4{font-family:"Roboto Condensed",sans-serif;font-weight:300;font-size:13px;line-height:16px;color:#ddd}
.news p{font-size:9.5px;line-height:15px;color:var(--footer-link);margin-top:4px}
.foot-brand{left:757px;top:21px;display:flex;align-items:center;gap:8px;opacity:.35}
.foot-brand .brand-mark{width:52px;height:52px;border:3px solid #999}
.foot-brand .brand-name{font-size:22px;color:#999}
.foot-links{left:727px;top:90px;font-size:10px;color:#fff;white-space:nowrap}
.foot-links span{margin:0 4px}
.copy{left:727px;top:108px;font-size:9.5px;color:#999;white-space:nowrap}
</style>
</head>
<body>
<div class="abs topbar"></div>
<header class="abs masthead"></header>
<div class="abs brand"><div class="brand-mark"></div><div class="brand-name">Harbor Circuits LLC</div></div>
<div class="abs callout-photo" role="img" aria-label="Technician with a desktop computer tower"></div>
<div class="abs callout">
  <h3>GOT PROBLEM IN YOUR PC?</h3>
  <p>GET IT FIXED NOW</p>
  <strong>CALL US AT (555) 214 7730</strong>
</div>
<nav class="abs nav"><ul>
  <li class="active">HOME</li><li>PC REPAIR &amp; SUPPORT</li><li>MANAGED SERVICE PACKAGES</li><li>COMPANY</li><li>BLOG</li><li>CONTACT</li>
</ul></nav>

<div class="abs page"></div>

<section class="abs hero">
  <h1>PC REPAIR &amp; SUPPORT</h1>
  <h2>There are many variations of passages.</h2>
  <ul>
    <li>Lorem Ipsum available, but the majority have suffered alteration</li>
    <li>in some form, by injected humour, or randomised words which</li>
    <li>don't look even slightly believable. If you are going to use a</li>
    <li>passage of Lorem Ipsum</li>
  </ul>
  <div class="more">For More info, <b>Click Here.</b></div>
  <div class="pkg">Packages</div>
  <div class="starts">Starts at</div>
  <svg class="arrow" width="60" height="22" viewBox="0 0 60 22"><path d="M2 12 C18 2 36 2 52 10" fill="none" stroke="#111" stroke-width="3"/><path d="M44 3 L56 12 L42 16 Z" fill="#111"/></svg>
  <div class="price"><span>$</span>30</div>
  <div class="abs hero-art" role="img" aria-label="Open laptop with tiny construction workers and a crane repairing it"></div>
</section>

<div class="abs tab tab-services">Our Services</div>
<div class="abs tab tab-welcome">Welcome to Harbor PC Services</div>

<aside class="abs services-box">
  <ul>
    <li>There are many variations of pas-</li>
    <li>sages of Lorem Ipsum available, but</li>
    <li>the majority have suffered alteration in</li>
    <li>some form, by injected humour, or</li>
    <li>randomised words which don't look</li>
    <li>even slightly believable. If you are</li>
    <li>going to use a passage of Lorem</li>
  </ul>
</aside>
<div class="abs testimonial">
  <h3>Testimonials</h3>
  <div class="who"><div class="avatar" role="img" aria-label="Customer portrait"></div><div><b>24.08.2012</b><br>Marisa<br>Easton, Ohio</div></div>
  <p class="quote">There are many variations of passages of Lorem Ipsum available, but the majority have suffered alteration in some form, by injected humour, or randomised words which don't look even slightly believable.</p>
  <span class="read">Read more testimonials here&gt;&gt;</span>
</div>

<div class="abs welcome">
  <p>Our mission at Harbor PC Services is simple. Commercial or residential, we are here to provide the customer with an affordable and practical computer repair solution.</p>
  <p>Anything from virus/spyware removal to laptop repairs, we work to provide you with a cost-effective IT support solution that not only makes sense technically, but also financially.</p>
  <p>Our A+ Certified Computer technicians provide you with the highest quality IT service solutions, quickly, to ensure minimal downtime.</p>
  <p>Our mission at Harbor PC Services is simple. Commercial or residential, we are here to provide the customer with an affordable and practical computer repair solution.</p>
  <p>Anything from virus/spyware removal to laptop repairs, we work to provide you with a cost-effective IT support solution that not only makes sense technically, but also financially.</p>
  <p>Our A+ Certified Computer technicians provide you with the highest quality IT service solutions, quickly, to ensure minimal downtime.</p>
</div>
<div class="abs rule"></div>
<section class="fixed">
  <h2>Looking For a Fixed Monthly Cost?</h2>
  <p>Looking for a cost-effective, comprehensive solution to your computer support and repair needs? Choose one of our managed service packages.</p>
</section>
<div class="abs btn" style="top:818px">Fixed Monthly Cost</div>
<div class="abs btn" style="top:855px">Dedicated IT Resources</div>
<div class="abs btn" style="top:891px">Fast Resources</div>
<div class="abs ad" role="img" aria-label="Specials advertisement space"></div>

<footer class="abs footer">
  <h3 style="left:167px;top:11px">Latest Blog Discussions</h3>
  <div class="abs blog">
    <a>There are many variations of passages of Lorem Ipsum available...</a>
    <a>There are many variations of passages of Lorem Ipsum available...</a>
    <a>There are many variations of passages of Lorem Ipsum available...</a>
  </div>
  <div class="abs vsep" style="left:432px"></div>
  <h3 style="left:451px;top:11px">Latest News</h3>
  <div class="abs news">
    <h4>Introducing New Managed Services Packages</h4>
    <p>There are many variations of passages of Lorem Ipsum available, but the majority have suffered alteration in some form,</p>
  </div>
  <div class="abs vsep" style="left:710px"></div>
  <div class="abs foot-brand"><div class="brand-mark"></div><div class="brand-name">Harbor Circuits LLC</div></div>
  <div class="abs foot-links">Home<span>|</span>PC Repair<span>|</span>Service<span>|</span>Company<span>|</span>Contact</div>
  <div class="abs copy">Copyright © 2010 Harbor . All rights reserved</div>
</footer>
</body>
</html>
```